Modern wordpress-enabled design wanted for translations agency serving large corporations

We are a translation agency and we only work for corporate clients and not private individuals. We are currently using the Larvesk wordpress theme and an upload feature called trobanex. It is important that prospective clients can upload their file. So we need a cool design for that kind of feature. We offer different kinds of translations tailored to the needs or global corporations. Corporate communications translations, legal translations, financial translations, healthcare translations, financial translations, audit translations.

```html
<!DOCTYPE html>
<html lang="en">
<head>
<meta charset="utf-8">
<title>Translation Agency</title>
<link href="https://fonts.googleapis.com/css2?family=Open+Sans:wght@300;400;600;700&display=swap" rel="stylesheet">
<style>
:root{
  --red:#e5432b;
  --dark:#1d2126;
  --darker:#15181c;
  --text:#333;
  --muted:#8a8f94;
  --line:#e3e3e3;
  --white:#fff;
}
*{box-sizing:border-box;margin:0;padding:0}
html,body{width:1200px;height:2188px;overflow:hidden}
body{font-family:"Open Sans",Arial,sans-serif;color:var(--text);background:var(--white);position:relative}
section,header,footer{position:absolute;left:0;width:1200px}

.site-header{top:0;height:88px;display:flex;align-items:center;justify-content:space-between;padding:0 40px;border-bottom:1px solid var(--line)}
.logo{font-size:34px;font-weight:700;letter-spacing:1px;color:#222}
.main-nav{display:flex;align-items:center;gap:6px;font-size:14px}
.main-nav a{color:#444;text-decoration:none;padding:10px 14px}
.main-nav a.active{background:var(--red);color:var(--white)}
.search-btn{width:38px;height:38px;background:var(--red);margin-left:14px;display:flex;align-items:center;justify-content:center}

.hero{top:88px;height:464px;overflow:hidden}
.hero-photo{position:absolute;inset:0;background:linear-gradient(100deg,#c9c4bd 0%,#e9e7e3 40%,#d3d6da 70%,#aeb3b8 100%)}
.hero h1{position:absolute;left:180px;top:290px;font-weight:400;font-size:46px;color:var(--white);text-shadow:0 2px 6px rgba(0,0,0,.35)}
.dots{display:flex;gap:8px;justify-content:center}
.dots span{width:9px;height:9px;border-radius:50%;background:rgba(255,255,255,.55)}
.dots span.on{background:var(--white)}
.hero .dots{position:absolute;left:0;right:0;top:424px}

.intro{top:552px;height:480px;display:flex;padding:40px 40px 0}
.section-title{font-size:22px;font-weight:700;text-transform:uppercase;color:#222;padding-bottom:12px;position:relative}
.section-title::after{content:"";position:absolute;left:0;bottom:0;width:40px;height:3px;background:var(--red)}
.who{width:400px}
.who p{font-size:13px;line-height:21px;color:var(--muted);margin-top:18px}
.btn{display:inline-block;background:var(--red);color:var(--white);font-size:12px;padding:9px 18px;margin-top:22px;text-transform:uppercase}
.services{margin-left:50px;width:670px}
.service-grid{display:grid;grid-template-columns:1fr 1fr;column-gap:40px;row-gap:34px;margin-top:28px}
.service{display:flex;gap:18px;padding-bottom:18px;border-bottom:1px solid var(--line)}
.service-icon{flex:0 0 50px;height:50px;border-radius:50%;background:#3a3f45;display:flex;align-items:center;justify-content:center}
.service-icon.hot{background:var(--red)}
.service h3{font-size:14px;font-weight:600;color:var(--red);line-height:20px}
.service p{font-size:12px;line-height:18px;color:var(--muted);margin-top:5px}

.testimonials{top:1032px;height:440px;overflow:hidden}
.testimonials-bg{position:absolute;inset:0;background:linear-gradient(180deg,#2b2f33,#1a1d20)}
.testimonials-head{position:absolute;top:40px;left:0;right:0;display:flex;align-items:center;justify-content:center;gap:22px;color:var(--white)}
.testimonials-head h2{font-size:26px;font-weight:700;letter-spacing:6px}
.testimonials-head .rule{width:150px;height:1px;background:rgba(255,255,255,.5)}
.cards{position:absolute;top:120px;left:70px;right:70px;display:flex;justify-content:space-between}
.card{width:310px;color:var(--white);text-align:center}
.avatar{width:66px;height:66px;margin:0 auto;background:linear-gradient(135deg,#8c8f92,#55595d);border:3px solid #fff}
.card-meta{margin-top:16px;font-size:13px;white-space:nowrap}
.card-role{color:var(--red);font-size:12px;margin-left:8px}
.quote{color:var(--red);font-size:34px;font-family:Georgia,serif;line-height:30px;margin-top:10px;height:26px}
.card p{font-size:12px;line-height:19px;color:#ddd}
.testimonials .dots{position:absolute;left:0;right:0;top:404px}

.clients{top:1472px;height:108px;display:flex;align-items:center;justify-content:space-around;padding:0 60px;border-bottom:1px solid var(--line)}
.client{display:flex;align-items:center;gap:8px;font-size:17px;font-weight:600;color:#555}
.client i{width:14px;height:14px;background:#777;display:block}

.world{top:1580px;height:272px;text-align:center;overflow:hidden}
.world h2{font-weight:400;font-size:30px;color:#333;margin-top:34px}
.world-map{position:absolute;left:260px;top:96px;width:680px;height:176px;background:radial-gradient(ellipse at 50% 55%,#a9cfd6 0%,#cfe4e6 45%,#f2f6f6 75%,#fff 100%)}

.tab{position:absolute;left:110px;top:1852px;width:140px;height:40px;background:var(--red);color:var(--white);font-size:15px;line-height:40px;text-align:center}

.site-footer{top:1892px;height:248px;background:var(--dark);color:#cfd2d5;display:flex;padding:26px 40px 0 110px}
.footer-col{width:240px}
.footer-col h4{font-size:15px;color:var(--white);font-weight:600;margin-bottom:14px}
.footer-col ul{list-style:none}
.footer-col li{font-size:12px;line-height:24px;display:flex;gap:8px;align-items:flex-start}
.menu li::before{content:"\203A";color:var(--red);font-size:16px;line-height:22px}
.tweets li{line-height:20px;margin-bottom:10px;padding-right:20px}
.mini-icon{flex:0 0 16px;height:16px;border-radius:50%;background:var(--red);margin-top:2px}
.contact li{line-height:20px;margin-bottom:12px}
.contact svg{flex:0 0 18px;margin-top:1px}
.form input,.form textarea{display:block;width:230px;height:26px;background:#2d3238;border:0;margin-bottom:8px;resize:none}
.form textarea{height:46px}
.form .submit{background:var(--red);color:var(--white);font-size:12px;padding:7px 18px;display:inline-block}
.social{position:absolute;right:40px;top:2100px;display:flex;gap:8px}
.social span{width:24px;height:24px;border-radius:50%;background:#4a5057;display:block}
.bottom-bar{position:absolute;top:2140px;left:0;width:1200px;height:48px;background:var(--darker);color:#8a8f94;font-size:11px;line-height:48px;padding-left:40px}
</style>
</head>
<body>
<header class="site-header">
  <div class="logo">LOGO</div>
  <nav class="main-nav">
    <a class="active">Home</a><a>Who We Are</a><a>Service</a><a>Testimonial</a><a>Blog</a><a>Contact Us</a>
    <span class="search-btn"><svg width="16" height="16" viewBox="0 0 16 16"><circle cx="6.5" cy="6.5" r="5" fill="none" stroke="#fff" stroke-width="2"/><line x1="10" y1="10" x2="15" y2="15" stroke="#fff" stroke-width="2"/></svg></span>
  </nav>
</header>

<section class="hero">
  <div class="hero-photo" role="img" aria-label="Photo of a smiling man working on a laptop in a bright office"></div>
  <h1>We are a translation agency</h1>
  <div class="dots"><span class="on"></span><span></span></div>
</section>

<section class="intro">
  <div class="who">
    <h2 class="section-title">Who We Are</h2>
    <p>We are a team of certified linguists who serve global corporations only. Every project is handled by native speakers with deep knowledge of the business field, reviewed by a second editor and delivered on time. Our clients rely on us for clear, accurate and confidential translations in more than forty languages.</p>
    <p>Upload your file, tell us the target languages and receive a quote within one business hour.</p>
    <span class="btn">Read More</span>
  </div>
  <div class="services">
    <h2 class="section-title">Our Service</h2>
    <div class="service-grid">
      <div class="service"><span class="service-icon hot"><svg width="22" height="22" viewBox="0 0 22 22"><rect x="3" y="3" width="16" height="16" fill="none" stroke="#fff" stroke-width="2"/></svg></span><div><h3>Corporate communications translations</h3><p>Reports, releases and internal notes written for every market you work in.</p></div></div>
      <div class="service"><span class="service-icon"><svg width="22" height="22" viewBox="0 0 22 22"><path d="M11 3v16M5 7h12M5 7l-3 7h6zM17 7l-3 7h6z" fill="none" stroke="#fff" stroke-width="1.8"/></svg></span><div><h3>Legal translations</h3><p>Contracts, filings and terms handled by lawyer linguists with care.</p></div></div>
      <div class="service"><span class="service-icon"><svg width="22" height="22" viewBox="0 0 22 22"><path d="M11 4v14M4 11h14" stroke="#fff" stroke-width="3"/></svg></span><div><h3>Healthcare translations</h3><p>Clinical, pharma and patient texts checked by medical experts.</p></div></div>
      <div class="service"><span class="service-icon"><svg width="22" height="22" viewBox="0 0 22 22"><path d="M4 18V10M9 18V6M14 18V12M19 18V4" stroke="#fff" stroke-width="2.5"/></svg></span><div><h3>Financial translations</h3><p>Statements, filings and investor material in every key language.</p></div></div>
      <div class="service"><span class="service-icon"><svg width="22" height="22" viewBox="0 0 22 22"><circle cx="11" cy="11" r="7" fill="none" stroke="#fff" stroke-width="2"/><path d="M11 7v8M8 9h5M8 13h5" stroke="#fff" stroke-width="1.5"/></svg></span><div><h3>Financial translations</h3><p>Annual reports and fund papers translated fast and in full.</p></div></div>
      <div class="service"><span class="service-icon"><svg width="22" height="22" viewBox="0 0 22 22"><path d="M5 12l4 4 8-9" fill="none" stroke="#fff" stroke-width="2.5"/></svg></span><div><h3>Audit translations</h3><p>Audit files and compliance records kept precise and confidential.</p></div></div>
    </div>
  </div>
</section>

<section class="testimonials">
  <div class="testimonials-bg" role="img" aria-label="Dark photo of an office interior"></div>
  <div class="testimonials-head">
    <svg width="10" height="16" viewBox="0 0 10 16"><path d="M8 2L2 8l6 6" fill="none" stroke="#fff" stroke-width="2"/></svg>
    <span class="rule"></span><h2>TESTIMONIAL</h2><span class="rule"></span>
    <svg width="10" height="16" viewBox="0 0 10 16"><path d="M2 2l6 6-6 6" fill="none" stroke="#fff" stroke-width="2"/></svg>
  </div>
  <div class="cards">
    <div class="card"><div class="avatar" role="img" aria-label="Client portrait"></div><div class="card-meta">Dale Morren<span class="card-role">Managing Director</span></div><div class="quote">&ldquo;</div><p>Fast, precise and always on time. Our legal team trusts them with every contract we sign abroad and the quality never drops.</p></div>
    <div class="card"><div class="avatar" role="img" aria-label="Client portrait"></div><div class="card-meta">Dale Morren<span class="card-role">Managing Director</span></div><div class="quote">&ldquo;</div><p>Fast, precise and always on time. Our legal team trusts them with every contract we sign abroad and the quality never drops.</p></div>
    <div class="card"><div class="avatar" role="img" aria-label="Client portrait"></div><div class="card-meta">Dale Morren<span class="card-role">Managing Director</span></div><div class="quote">&ldquo;</div><p>Fast, precise and always on time. Our legal team trusts them with every contract we sign abroad and the quality never drops.</p></div>
  </div>
  <div class="dots"><span></span><span class="on"></span><span></span></div>
</section>

<section class="clients">
  <span class="client"><i></i>Northpeak</span>
  <span class="client"><i></i>Velora</span>
  <span class="client"><i></i>Quintar</span>
  <span class="client"><i></i>Halvex</span>
  <span class="client"><i></i>Ostrano</span>
  <span class="client"><i></i>Mirelle</span>
</section>

<section class="world">
  <h2>We are all over in the World</h2>
  <div class="world-map" role="img" aria-label="World map with office location pins"></div>
</section>

<div class="tab">Get In Touch</div>

<footer class="site-footer">
  <div class="footer-col">
    <h4>Main menu</h4>
    <ul class="menu"><li>Home</li><li>About Us</li><li>Pricing</li><li>Services</li><li>Media</li></ul>
  </div>
  <div class="footer-col">
    <h4>Latest Tweets</h4>
    <ul class="tweets">
      <li><span class="mini-icon"></span><span>New legal glossary now live for all clients</span></li>
      <li><span class="mini-icon"></span><span>We now translate into twelve more languages</span></li>
    </ul>
  </div>
  <div class="footer-col">
    <h4>Contact Us</h4>
    <ul class="contact">
      <li><svg width="18" height="18" viewBox="0 0 18 18"><path d="M9 1a5 5 0 0 1 5 5c0 4-5 10-5 10S4 10 4 6a5 5 0 0 1 5-5z" fill="#e5432b"/><circle cx="9" cy="6" r="2" fill="#1d2126"/></svg><span>1420 Harbor Lane West<br>Suite 300</span></li>
      <li><svg width="18" height="18" viewBox="0 0 18 18"><path d="M4 2l3 3-2 2c1 2 3 4 5 5l2-2 3 3-2 2C8 15 3 10 2 4z" fill="#e5432b"/></svg><span>(555) 014-2280</span></li>
      <li><svg width="18" height="18" viewBox="0 0 18 18"><rect x="2" y="4" width="14" height="10" fill="#e5432b"/><path d="M2 4l7 6 7-6" fill="none" stroke="#1d2126" stroke-width="1.5"/></svg><span>hello@agency.example</span></li>
    </ul>
  </div>
  <div class="footer-col form">
    <h4>Quick Contact</h4>
    <input aria-label="Name"><input aria-label="Email"><textarea aria-label="Message"></textarea>
    <span class="submit">SUBMIT</span>
  </div>
</footer>
<div class="social"><span></span><span></span><span></span><span></span><span></span><span></span></div>
<div class="bottom-bar">&copy; 2024 Translation Agency. All rights reserved.</div>
</body>
</html>
```